El Molcajete Burrito Van Website

We would like a website design for a local taco truck. El Molcajete is at the top of the food truck scene in Northern CA. Often hired by celebrities in San Francisco, they travel to homes of the rich and famous to bring their flavors of Mexico directly to them.
https://www.plinvoramaps.example/place/elmolcajete-burrito-van-photos
Target Market(s)
Local catering jobs
Number of Pages Required
3 page
Requirements
Must have
- Clients logo

```html
<!DOCTYPE html>
<html lang="en">
<head>
<meta charset="utf-8">
<title>El Molcajete Burrito Van</title>
<link href="https://fonts.googleapis.com/css2?family=Roboto+Condensed:wght@400;700&family=Roboto:wght@400;500&family=Great+Vibes&display=swap" rel="stylesheet">
<style>
:root{
  --red:#c8302b;
  --red-dark:#8e1a16;
  --hero:#7a1e17;
  --ink:#151515;
  --text:#555;
  --light:#f6f6f6;
  --field:#efefef;
  --footer:#1b1b1b;
  --white:#fff;
}
*{margin:0;padding:0;box-sizing:border-box}
html,body{width:1200px;height:3807px;overflow:hidden}
body{position:relative;font-family:'Roboto',sans-serif;color:var(--text);background:var(--white)}
.abs{position:absolute}
.cond{font-family:'Roboto Condensed',sans-serif}
/* hero */
.hero{left:0;top:0;width:1200px;height:795px;background:radial-gradient(circle at 70% 55%,#8f2a20 0%,var(--hero) 45%,#5e150f 100%)}
.topbar{left:0;top:33px;width:1200px;height:79px;background:var(--white)}
.brand{left:108px;top:52px;display:flex;align-items:center;gap:10px;font:700 22px 'Roboto Condensed',sans-serif;color:var(--red)}
.brand i{width:30px;height:30px;border-radius:50%;background:var(--red);display:block}
.nav{left:444px;top:62px;display:flex;gap:0;font-size:15px;color:var(--ink)}
.nav span{margin-right:53px}
.call{left:906px;top:52px;display:flex;align-items:center;gap:18px;font:500 15px 'Roboto',sans-serif;color:var(--ink)}
.ico{width:42px;height:42px;border-radius:50%;background:var(--red);display:flex;align-items:center;justify-content:center}
.welcome{left:110px;top:305px;font:36px 'Great Vibes',cursive;color:var(--white)}
.title{left:110px;top:350px;font:700 60px 'Roboto Condensed',sans-serif;color:var(--white);letter-spacing:1px}
.lead{left:112px;top:428px;width:390px;font-size:15px;line-height:26px;color:#f4e6e4}
.btn{display:flex;align-items:center;justify-content:space-between;padding:0 6px 0 24px;border-radius:30px;background:linear-gradient(90deg,var(--red-dark),var(--red));color:var(--white);font:700 16px 'Roboto Condensed',sans-serif}
.btn b{width:40px;height:40px;border-radius:50%;background:var(--white);display:flex;align-items:center;justify-content:center}
.ring{left:617px;top:218px;width:466px;height:466px;border-radius:50%;background:#9a2f24}
.photo{background:linear-gradient(135deg,#c9a24a,#7a5a35 50%,#2b2b2b)}
.hero-photo{left:640px;top:241px;width:420px;height:420px;border-radius:50%}
/* about */
.h2{font:700 36px 'Roboto Condensed',sans-serif;color:var(--ink);text-align:center}
.h2 em{font-style:normal;color:var(--red)}
.h2::before,.h2::after{content:"";position:absolute;left:50%;transform:translateX(-50%);width:108px;height:2px;background:#888}
.h2::before{top:-10px}.h2::after{bottom:-8px}
.about-text{left:652px;top:1008px;width:428px;text-align:center;font-size:15px;line-height:25.7px}
/* menu */
.menu{left:0;top:1482px;width:1200px;height:1201px;background:var(--light)}
.item{left:151px;width:628px}
.item h3{font:700 23px 'Roboto Condensed',sans-serif;color:var(--ink)}
.item .price{position:absolute;right:0;top:-8px;font:700 32px 'Roboto Condensed',sans-serif;color:var(--red)}
.item p{margin-top:8px;font-size:15px;line-height:25px;color:#666}
.dish{left:853px;width:223px;height:215px;border-radius:10px}
/* contact */
.field{background:var(--field);font-size:15px;color:#888;padding:0 28px;display:flex;align-items:center}
.info{display:flex;align-items:flex-start;gap:18px;font-size:15px;line-height:26px;color:var(--ink)}
.info svg{flex:none;margin-top:5px}
.soc{display:flex;gap:8px}
.soc i{width:40px;height:40px;border-radius:50%;border:2px solid var(--red);display:block}
.soc i:first-child{background:var(--red)}
/* footer */
.footer{left:0;top:3352px;width:1200px;height:455px;background:linear-gradient(135deg,#202020,#141414)}
.fh{font:700 25px 'Roboto Condensed',sans-serif;color:var(--white)}
.hours{left:442px;top:3472px;width:240px;font-size:16px;color:var(--white);line-height:30px}
.hours div{display:flex}.hours span{width:135px}
.finfo{color:var(--white)}
</style>
</head>
<body>
<!-- hero -->
<div class="abs hero"></div>
<div class="abs topbar"></div>
<div class="abs brand"><i></i>El Molcajete</div>
<nav class="abs nav"><span>Home</span><span>About</span><span>Menu</span><span>Blog</span><span>Contact</span></nav>
<div class="abs call"><div class="ico"><svg width="18" height="18" viewBox="0 0 24 24"><path fill="#fff" d="M6.6 10.8a15 15 0 006.6 6.6l2.2-2.2c.3-.3.7-.4 1-.2 1.1.4 2.3.6 3.6.6.6 0 1 .4 1 1V20c0 .6-.4 1-1 1A17 17 0 013 4c0-.6.4-1 1-1h3.5c.6 0 1 .4 1 1 0 1.3.2 2.5.6 3.6.1.3 0 .7-.2 1z"/></svg></div>+1 555 014 2290</div>
<div class="abs welcome">Welcome To</div>
<h1 class="abs title">EL MOLCAJETE</h1>
<p class="abs lead">Lorem ipsum dolor sit amet, consectetur adipiscing elit, sed do eiusmod tempor incididunt ut labore et dolore magna aliqua.</p>
<div class="abs btn" style="left:112px;top:528px;width:158px;height:52px">Order Now<b><svg width="16" height="16" viewBox="0 0 24 24"><path fill="none" stroke="#c8302b" stroke-width="2.5" d="M4 12h15M13 6l6 6-6 6"/></svg></b></div>
<div class="abs ring"></div>
<div class="abs photo hero-photo" role="img" aria-label="Photo of two soft tacos with shredded meat, avocado and lime"></div>

<!-- about -->
<div class="abs photo" style="left:333px;top:855px;width:80px;height:160px;border-radius:40px;background:linear-gradient(#f5c33a,#f0a81e)" role="img" aria-label="Lemon slices"></div>
<div class="abs photo" style="left:112px;top:888px;width:252px;height:436px" role="img" aria-label="Photo of a burrito cut in half on a board"></div>
<div class="abs photo" style="left:374px;top:962px;width:251px;height:436px;background:linear-gradient(135deg,#b0784a,#6b3b22 50%,#222)" role="img" aria-label="Photo of a grilled burrito with beef filling"></div>
<div class="abs" style="left:0;top:1270px;width:155px;height:175px;border-radius:50%;background:linear-gradient(135deg,#d9a441,#9c3a22)" role="img" aria-label="Photo of tacos"></div>
<div class="abs" style="left:1015px;top:1308px;width:185px;height:230px;border-radius:40% 0 0 40%;background:linear-gradient(135deg,#4e8a2f,#d23a24 50%,#f0b93a)" role="img" aria-label="Photo of a crunchy taco"></div>
<h2 class="abs h2" style="left:655px;top:930px;width:378px">ABOUT <em>EL MOLCAJETE</em></h2>
<p class="abs about-text">Lorem ipsum dolor sit amet, consectetur adipiscing elit, sed do eiusmod tempor incididunt ut labore et dolore magna aliqua. Quis ipsum suspendisse ultrices gravida. Risus commodo viverra maecenas accumsan lacus vel facilisis. Lorem ipsum dolor sit amet, consectetur adipiscing elit, sed do eiusmod tempor incididunt ut labore et dolore magna aliqua. Quis ipsum suspendisse ultrices gravida. Risus commodo viverra maecenas accumsan lacus vel facilisis. Lorem ipsum dolor sit amet, consectetur adipiscing elit, sed</p>
<div class="abs btn" style="left:770px;top:1259px;width:158px;height:52px">Learn More<b><svg width="16" height="16" viewBox="0 0 24 24"><path fill="none" stroke="#c8302b" stroke-width="2.5" d="M4 12h15M13 6l6 6-6 6"/></svg></b></div>

<!-- menu -->
<div class="abs menu"></div>
<h2 class="abs h2" style="left:500px;top:1540px;width:200px">OUR <em>MENU</em></h2>
<div class="abs item" style="top:1688px"><h3>Tacos</h3><span class="price">$2.00</span><p>Lorem ipsum dolor sit amet, consectetur adipiscing elit, sed do eiusmod tempor incididunt ut labore et dolore magna aliqua. Quis ipsum suspendisse ultrices gravida.</p></div>
<div class="abs item" style="top:1796px"><h3>Tacos Regular</h3><span class="price">$6.00</span><p>Lorem ipsum dolor sit amet, consectetur adipiscing elit, sed do eiusmod tempor incididunt ut labore et dolore magna aliqua. Quis ipsum suspendisse ultrices gravida.</p></div>
<div class="abs item" style="top:1902px"><h3>Super Burrito</h3><span class="price">$7.00</span><p>Lorem ipsum dolor sit amet, consectetur adipiscing elit, sed do eiusmod tempor incididunt ut labore et dolore magna aliqua. Quis ipsum suspendisse ultrices gravida.</p></div>
<div class="abs item" style="top:2007px"><h3>Burrito Vegetariano</h3><span class="price">$6.50</span><p>Lorem ipsum dolor sit amet, consectetur adipiscing elit, sed do eiusmod tempor incididunt ut labore et dolore magna aliqua. Quis ipsum suspendisse ultrices gravida.</p></div>
<div class="abs item" style="top:2138px"><h3>Torta Regular</h3><span class="price">$6.50</span><p>Lorem ipsum dolor sit amet, consectetur adipiscing elit, sed do eiusmod tempor incididunt ut labore et dolore magna aliqua. Quis ipsum suspendisse ultrices gravida.</p></div>
<div class="abs item" style="top:2242px"><h3>Torta Combinada</h3><span class="price">$7.00</span><p>Lorem ipsum dolor sit amet, consectetur adipiscing elit, sed do eiusmod tempor incididunt ut labore et dolore magna aliqua. Quis ipsum suspendisse ultrices gravida.</p></div>
<div class="abs item" style="top:2372px"><h3>Quesadilla Regular</h3><span class="price">$7.00</span><p>Lorem ipsum dolor sit amet, consectetur adipiscing elit, sed do eiusmod tempor incididunt ut labore et dolore magna aliqua. Quis ipsum suspendisse ultrices gravida.</p></div>
<div class="abs item" style="top:2502px"><h3>Quesadilla Vegetariano</h3><span class="price">$6.00</span><p>Lorem ipsum dolor sit amet, consectetur adipiscing elit, sed do eiusmod tempor incididunt ut labore et dolore magna aliqua. Quis ipsum suspendisse ultrices gravida.</p></div>
<div class="abs photo dish" style="top:1645px;background:linear-gradient(135deg,#e2b43a,#8a4a25 55%,#1e1e1e)" role="img" aria-label="Photo of crunchy tacos"></div>
<div class="abs photo dish" style="top:1893px;background:linear-gradient(135deg,#c98a4a,#e9dcc4 50%,#3a2a22)" role="img" aria-label="Photo of burritos on a plate"></div>
<div class="abs photo dish" style="top:2143px;background:linear-gradient(135deg,#d19a55,#f1ead9 55%,#6b7a45)" role="img" aria-label="Photo of a torta sandwich"></div>
<div class="abs photo dish" style="top:2391px;background:linear-gradient(135deg,#f2efe8,#e8c98a 50%,#4a3020)" role="img" aria-label="Photo of quesadilla wedges with salsa"></div>

<!-- contact -->
<h2 class="abs h2" style="left:480px;top:2752px;width:240px">CONTACT <em>US</em></h2>
<p class="abs" style="left:200px;top:2826px;width:800px;text-align:center;font-size:15px;line-height:26px">Lorem ipsum dolor sit amet, consectetur adipiscing elit, sed do eiusmod tempor incididunt ut labore et dolore magna aliqua. Quis ipsum suspendisse ultrices gravida.</p>
<div class="abs field" style="left:138px;top:2920px;width:255px;height:52px">First Name</div>
<div class="abs field" style="left:410px;top:2920px;width:255px;height:52px">Late Name</div>
<div class="abs field" style="left:138px;top:2988px;width:255px;height:52px">Email</div>
<div class="abs field" style="left:409px;top:2988px;width:255px;height:52px">Phone</div>
<div class="abs field" style="left:138px;top:3057px;width:526px;height:140px;align-items:flex-start;padding-top:16px">Messages</div>
<div class="abs btn" style="left:136px;top:3220px;width:137px;height:57px;justify-content:center;padding:0;font-size:15px">Submit</div>
<h3 class="abs cond" style="left:742px;top:2930px;font-size:26px;color:var(--ink)">Get &nbsp;in Touch</h3>
<div class="abs info" style="left:748px;top:2996px;width:320px">
<svg width="14" height="18" viewBox="0 0 14 18"><path fill="#c8302b" d="M7 0a7 7 0 00-7 7c0 5 7 11 7 11s7-6 7-11a7 7 0 00-7-7zm0 9.5A2.5 2.5 0 117 4.5a2.5 2.5 0 010 5z"/></svg>
<span>199 /b El Molcajete consectetur adipiscing elit, sed do eiusmod tempor</span></div>
<div class="abs info" style="left:748px;top:3060px"><svg width="17" height="17" viewBox="0 0 24 24"><path fill="#c8302b" d="M6.6 10.8a15 15 0 006.6 6.6l2.2-2.2c.3-.3.7-.4 1-.2 1.1.4 2.3.6 3.6.6.6 0 1 .4 1 1V20c0 .6-.4 1-1 1A17 17 0 013 4c0-.6.4-1 1-1h3.5c.6 0 1 .4 1 1 0 1.3.2 2.5.6 3.6.1.3 0 .7-.2 1z"/></svg><span>+1 555 014 2290</span></div>
<div class="abs info" style="left:748px;top:3102px"><svg width="18" height="14" viewBox="0 0 18 14"><path fill="#c8302b" d="M0 0h18v2L9 8 0 2zM0 4l9 6 9-6v10H0z"/></svg><span>info@elmolcajete.example</span></div>
<div class="abs soc" style="left:745px;top:3157px"><i></i><i></i><i></i><i></i></div>

<!-- footer -->
<div class="abs footer"></div>
<div class="abs" style="left:130px;top:3500px;display:flex;align-items:center;gap:10px;font:700 26px 'Roboto Condensed',sans-serif;color:var(--red)"><i style="width:32px;height:32px;border-radius:50%;background:var(--red);display:block"></i>El Molcajete</div>
<div class="abs soc" style="left:168px;top:3625px;gap:6px"><i style="width:22px;height:22px;background:var(--red)"></i><i style="width:22px;height:22px;background:var(--red)"></i><i style="width:22px;height:22px;background:var(--red)"></i><i style="width:22px;height:22px;background:var(--red)"></i></div>
<h3 class="abs fh" style="left:440px;top:3422px">OPENING HOURS</h3>
<div class="abs hours">
<div><span>Monday</span>8am-10pm</div>
<div><span>Tuesday</span>8am-10pm</div>
<div><span>Wednesday</span>8am-10pm</div>
<div><span>Thursday</span>8am-10pm</div>
<div><span>Friday</span>11am-12pm</div>
<div><span>Saturday</span>11am-12pm</div>
<div><span>Sunday</span>11am-12pm</div>
</div>
<h3 class="abs fh" style="left:767px;top:3420px">CONNECT WITH US</h3>
<div class="abs info finfo" style="left:770px;top:3467px;width:310px"><svg width="14" height="18" viewBox="0 0 14 18"><path fill="#c8302b" d="M7 0a7 7 0 00-7 7c0 5 7 11 7 11s7-6 7-11a7 7 0 00-7-7zm0 9.5A2.5 2.5 0 117 4.5a2.5 2.5 0 010 5z"/></svg><span>199 /b El Molcajete consectetur adipiscing elit, sed do eiusmod tempor</span></div>
<div class="abs info finfo" style="left:770px;top:3531px"><svg width="17" height="17" viewBox="0 0 24 24"><path fill="#c8302b" d="M6.6 10.8a15 15 0 006.6 6.6l2.2-2.2c.3-.3.7-.4 1-.2 1.1.4 2.3.6 3.6.6.6 0 1 .4 1 1V20c0 .6-.4 1-1 1A17 17 0 013 4c0-.6.4-1 1-1h3.5c.6 0 1 .4 1 1 0 1.3.2 2.5.6 3.6.1.3 0 .7-.2 1z"/></svg><span>+1 555 014 2290</span></div>
<div class="abs info finfo" style="left:770px;top:3574px"><svg width="18" height="14" viewBox="0 0 18 14"><path fill="#c8302b" d="M0 0h18v2L9 8 0 2zM0 4l9 6 9-6v10H0z"/></svg><span>info@elmolcajete.example</span></div>
<div class="abs" style="left:100px;top:3710px;width:1000px;height:1px;background:#333"></div>
<p class="abs" style="left:0;top:3745px;width:1200px;text-align:center;font-size:15px;color:var(--white)">©Copyrights 2022 &nbsp;El Molcajete | &nbsp;&nbsp;All Rights Reserved</p>
</body>
</html>
```